VelloTek needs web site design

We need a web site design for our product called 'VelloTek'. We develop an asset management system that can manage all kind of assets. Currently we have a logo theme and would like to use similar color scheme; the content concept is pretty much in http://tdalwynne.net but the product was called "Kestel Suite" at the time and is now called "VelloTek". Vello means Vast Equipment Ledger Logging Organizer.
Please use generic image for asset (not just bridges) e.g buildings, trucks, powerlines. train, bus, lightrail etc..
Please emphazise on the data management and security, and distributed networking.

the new website address is https://www.vellotek.example/

name on business card

Thomas Dalwynne 555-014-7392
Principal Architect / Software Engineer

Tara Dalwynne 555-018-2641
Software Engineer

Coding

Coded - Design and coding required

Number of Pages Required

1 page

```html
<!DOCTYPE html>
<html lang="en">
<head>
<meta charset="utf-8">
<title>VelloTek Business Card</title>
<link href="https://fonts.googleapis.com/css2?family=Montserrat:wght@400;500;700;800&display=swap" rel="stylesheet">
<style>
  :root {
    --bg: #ededed;
    --gold: #d3ac55;
    --white: #ffffff;
    --brand-blue: #2f3c9e;
    --card-blue: #3a47a6;
    --ink-soft: rgba(255,255,255,0.85);
  }
  * { margin: 0; padding: 0; box-sizing: border-box; }
  html, body { width: 1200px; height: 800px; overflow: hidden; }
  body {
    background: var(--bg);
    font-family: "Montserrat", Arial, sans-serif;
    display: flex;
    align-items: center;
    justify-content: center;
    gap: 60px;
  }
  .card {
    width: 500px;
    height: 286px;
    border-radius: 3px;
    box-shadow: 0 18px 40px rgba(0,0,0,0.18);
    overflow: hidden;
    display: flex;
  }
  /* Front */
  .card-front { background: var(--white); }
  .front-brand {
    width: 43%;
    display: flex;
    flex-direction: column;
    justify-content: center;
    padding-left: 42px;
  }
  .brand-line { display: flex; align-items: center; gap: 8px; }
  .brand-square {
    width: 22px; height: 22px;
    border: 3px solid var(--brand-blue);
  }
  .brand-name {
    font-weight: 700;
    font-size: 28px;
    color: var(--brand-blue);
    letter-spacing: -0.5px;
  }
  .brand-tag {
    font-size: 8.5px;
    font-weight: 500;
    letter-spacing: 1.2px;
    color: var(--gold);
    margin-top: 3px;
    margin-left: 30px;
  }
  .front-contacts {
    flex: 1;
    background: var(--gold);
    color: var(--white);
    display: flex;
    flex-direction: column;
    justify-content: center;
    gap: 26px;
    padding-left: 40px;
  }
  .person-name { font-weight: 800; font-size: 16px; letter-spacing: 0.3px; }
  .person-role { font-size: 8px; color: var(--ink-soft); margin-top: 2px; }
  .contact-row {
    display: flex; align-items: center; gap: 6px;
    font-size: 8px; margin-top: 6px;
  }
  .contact-row + .contact-row { margin-top: 3px; }
  .contact-icon { width: 10px; height: 10px; flex: none; }
  /* Back */
  .card-back {
    background: linear-gradient(120deg, var(--card-blue) 0%, #4552ad 55%, #3a47a6 100%);
    align-items: center;
    justify-content: center;
    flex-direction: column;
  }
  .card-back .brand-square { border-color: var(--white); width: 34px; height: 34px; border-width: 4px; }
  .card-back .brand-name { color: var(--white); font-size: 44px; }
  .card-back .brand-line { gap: 12px; }
  .card-back .brand-tag { color: var(--white); font-size: 13px; margin-left: 46px; letter-spacing: 1.6px; }
</style>
</head>
<body>
  <section class="card card-front">
    <div class="front-brand">
      <div class="brand-line">
        <span class="brand-square"></span>
        <span class="brand-name">VelloTek</span>
      </div>
      <div class="brand-tag">ASSET MANAGEMENT</div>
    </div>
    <div class="front-contacts">
      <div class="person">
        <div class="person-name">THOMAS DALWYNNE</div>
        <div class="person-role">Principal Architect / Software Engineer</div>
        <div class="contact-row">
          <svg class="contact-icon" viewBox="0 0 10 10"><circle cx="5" cy="5" r="5" fill="#fff"/><path d="M3.3 2.6l1 1-0.5 0.6a3.5 3.5 0 0 0 1.9 1.9l0.6-0.5 1 1-0.7 0.8C4.8 7.2 2.8 5.2 2.6 3.3z" fill="#d3ac55"/></svg>
          <span>555-014-7392</span>
        </div>
        <div class="contact-row">
          <svg class="contact-icon" viewBox="0 0 10 10"><circle cx="5" cy="5" r="5" fill="#fff"/><rect x="2.6" y="3.3" width="4.8" height="3.4" fill="#d3ac55"/><path d="M2.6 3.3L5 5.2 7.4 3.3" stroke="#fff" stroke-width="0.6" fill="none"/></svg>
          <span>thomas@vellotek.example</span>
        </div>
      </div>
      <div class="person">
        <div class="person-name">TARA DALWYNNE</div>
        <div class="person-role">Software Engineer</div>
        <div class="contact-row">
          <svg class="contact-icon" viewBox="0 0 10 10"><circle cx="5" cy="5" r="5" fill="#fff"/><path d="M3.3 2.6l1 1-0.5 0.6a3.5 3.5 0 0 0 1.9 1.9l0.6-0.5 1 1-0.7 0.8C4.8 7.2 2.8 5.2 2.6 3.3z" fill="#d3ac55"/></svg>
          <span>555-018-2641</span>
        </div>
        <div class="contact-row">
          <svg class="contact-icon" viewBox="0 0 10 10"><circle cx="5" cy="5" r="5" fill="#fff"/><rect x="2.6" y="3.3" width="4.8" height="3.4" fill="#d3ac55"/><path d="M2.6 3.3L5 5.2 7.4 3.3" stroke="#fff" stroke-width="0.6" fill="none"/></svg>
          <span>tara@vellotek.example</span>
        </div>
      </div>
    </div>
  </section>

  <section class="card card-back">
    <div>
      <div class="brand-line">
        <span class="brand-square"></span>
        <span class="brand-name">VelloTek</span>
      </div>
      <div class="brand-tag">ASSET MANAGEMENT</div>
    </div>
  </section>
</body>
</html>
```